Dental Business Card Design w/logo

Classic, elegant w/a touch of contemporary
Upscale dental facility located in Modesto CA
Specializing in restorative & general dentistry
Providing exceptional customer service to the community
Updates

I prefer script and not bold writing
If you can use the phone; fax and email icons instead of spelling them out, it would be great
No bold colors
Classy and elegant
In the back of the card I would like to see something like this
Your Next Appointment:
Mon     Tue    Wed    Thur (a box next to each of them for marking)
Date:_______________ at_____________ AM    PM  (a box next to them for marking)

Thank you

Target Market(s)

Well established professional

Industry/Entity Type

Dental

Contact Information for Business Card

Velorine Tamsuki DMD
4176 Larchmont Rd
Suite D7
Modesto, CA 95368

Office: 209-731-5092
Fax: 209-731-8247
Email: tamsukidmd@brivelmail.test

Requirements
Must have
• Unique classic logo
An easily repeatable design that can be used on letterhead and envelopes
Nice to have
• My initials incorporated into unique design
Should not have
• No cartoons or cheesy themes. This is a practice for the well established and professional individual.

```html
<!DOCTYPE html>
<html lang="en">
<head>
<meta charset="utf-8">
<title>Appointment Card – Velorine Tamsuki DMD</title>
<link rel="stylesheet" href="https://fonts.googleapis.com/css2?family=Jost:wght@300;400&display=swap">
<style>
  :root {
    --page: #ffffff;
    --ink: #111111;
    --frame: #555555;
    --mist: #c4e0e2;
  }
  * { margin: 0; padding: 0; box-sizing: border-box; }
  html, body {
    width: 1200px; height: 900px; overflow: hidden;
    background: var(--page);
  }
  .canvas { position: relative; width: 1200px; height: 900px; }
  .card {
    position: absolute; left: 346px; top: 14px;
    width: 503px; height: 871px;
    border: 1px solid var(--frame);
    background: var(--page);
    font-family: "Jost", "Futura", sans-serif;
    color: var(--ink);
  }
  .practice-name {
    position: absolute; left: 0; right: 0; top: 170px;
    text-align: center;
    font-weight: 400; font-size: 30px; letter-spacing: 0.5px;
    color: var(--mist);
  }
  .heading {
    position: absolute; left: 0; right: 0; top: 362px;
    text-align: center;
    font-weight: 300; font-size: 38px; letter-spacing: -0.5px;
  }
  .days {
    position: absolute; left: 161px; top: 414px;
    list-style: none;
  }
  .days li {
    display: flex; align-items: center;
    height: 43.6px;
    font-weight: 300; font-size: 30px; letter-spacing: -0.3px;
  }
  .box {
    display: inline-block; width: 18px; height: 18px;
    border: 2px solid var(--ink);
    margin-right: 12px; flex: none;
  }
  .line {
    position: absolute; display: flex; align-items: flex-end;
    font-weight: 300; font-size: 30px; letter-spacing: -0.3px;
    white-space: nowrap;
  }
  .line.date { left: 69px; top: 670px; }
  .line.time { left: 46px; top: 712px; }
  .blank {
    display: inline-block; height: 26px;
    border-bottom: 1.5px solid var(--ink);
    margin-bottom: 7px;
  }
  .date .blank { width: 300px; }
  .time .blank { width: 218px; margin-right: 8px; }
  .time .box { margin: 0 0 9px 8px; }
  .time .pm { margin-left: 30px; }
  .notice {
    position: absolute; left: 0; right: 0; top: 788px;
    text-align: center;
    font-weight: 300; font-size: 20.5px; line-height: 30px; letter-spacing: -0.3px;
  }
</style>
</head>
<body>
<div class="canvas">
  <section class="card">
    <div class="practice-name">Velorine Tamsuki DMD</div>
    <h1 class="heading">Your Next Appointment:</h1>
    <ul class="days">
      <li><span class="box"></span>Monday</li>
      <li><span class="box"></span>Tuesday</li>
      <li><span class="box"></span>Wednesday</li>
      <li><span class="box"></span>Thursday</li>
      <li><span class="box"></span>Friday</li>
    </ul>
    <div class="line date">Date:<span class="blank"></span></div>
    <div class="line time">at<span class="blank"></span>AM<span class="box"></span><span class="pm">PM</span><span class="box"></span></div>
    <p class="notice">If unable to keep this appointment kindly give 48 hours<br>notice, otherwise a charge will be made for time reserved.</p>
  </section>
</div>
</body>
</html>
```